Flyer for Lawnmowing and gardening business

We are a lawn mowing and gardening business needing a flyer designed listing our services and business info.
The flyer should include all business information and contact details as below.

Lawn mowing
Gardening
Green waste removal
Pruning
Weeding
Vegetable Garden Creation

Phone number:0481657240

As well as the logo provided

Target Market(s)

Local people wanting someone to care for their garden.

Industry/Entity Type

Gardener

Font styles to use
Serif

Requirements
Must have
• Business Logo
• All business info and services provided. EG
• Lawn mowing
• Gardening
• Green waste removal
• Pruning
• Weeding
• Vegetable Garden Creation
• Phone number:0481657240
Nice to have
• Earthy tones, clean and simple flyer design

```html
<!DOCTYPE html>
<html lang="en">
<head>
<meta charset="utf-8">
<title>Greenfield Yard Co – Lawn Mowing and Gardening Flyer</title>
<link href="https://fonts.googleapis.com/css2?family=Oswald:wght@300;700&display=swap" rel="stylesheet">
<style>
  :root {
    --lawn-light: #8fc548;
    --lawn-mid: #5f9a2c;
    --tree-dark: #29401d;
    --accent-green: #8cc63f;
    --earth-light: #c98a55;
    --earth-mid: #9a5a2e;
    --earth-dark: #6b3a1c;
    --paper: #ffffff;
    --brand-green: #3b5a24;
  }
  * { margin: 0; padding: 0; box-sizing: border-box; }
  html, body { width: 1200px; height: 2536px; overflow: hidden; background: var(--paper); }
  .flyer { position: relative; width: 1200px; height: 2536px; overflow: hidden; background: var(--paper); }

  .photo-lawn {
    position: absolute; left: 0; top: 0; width: 1200px; height: 1460px;
    background: linear-gradient(180deg, var(--tree-dark) 0%, #3f6a2a 30%, var(--lawn-mid) 55%, var(--lawn-light) 80%, var(--lawn-mid) 100%);
    clip-path: polygon(0 0, 100% 0, 100% 1100px, 0 1420px);
  }
  .photo-earthworks {
    position: absolute; left: 0; top: 1080px; width: 1200px; height: 1020px;
    background: linear-gradient(180deg, #4f6b34 0%, #8a6a40 25%, var(--earth-light) 55%, var(--earth-mid) 100%);
  }
  .bands { position: absolute; left: 0; top: 0; width: 1200px; height: 2536px; }

  .services {
    position: absolute; left: 0; top: 60px; width: 1200px;
    display: flex; flex-direction: column; align-items: center;
    font-family: "Oswald", sans-serif; color: var(--paper); text-transform: uppercase;
    text-shadow: 0 3px 8px rgba(0,0,0,0.35); line-height: 1;
  }
  .services .bold { font-weight: 700; font-size: 128px; letter-spacing: 2px; }
  .services .light { font-weight: 300; font-size: 84px; letter-spacing: 1px; }
  .services .rule { width: 640px; height: 6px; background: var(--paper); margin: 14px 0 12px; box-shadow: 0 3px 8px rgba(0,0,0,0.3); }
  .services .gap { height: 14px; }

  .contact-label, .contact-number { font-family: "Oswald", sans-serif; text-transform: uppercase; }

  .brand {
    position: absolute; left: 0; top: 2290px; width: 1200px;
    display: flex; align-items: center; justify-content: center; gap: 28px;
  }
  .brand-dot { width: 56px; height: 56px; border-radius: 50%; background: var(--brand-green); }
  .brand-name {
    font-family: "Oswald", sans-serif; font-weight: 700; font-size: 96px;
    color: var(--brand-green); text-transform: uppercase; letter-spacing: 2px; line-height: 1;
  }
</style>
</head>
<body>
<main class="flyer">
  <div class="photo-earthworks" role="img" aria-label="Photo of earthmoving machines levelling a red dirt site"></div>
  <div class="photo-lawn" role="img" aria-label="Photo of a freshly striped green lawn with trees behind"></div>

  <svg class="bands" viewBox="0 0 1200 2536" aria-hidden="true">
    <polygon points="0,1420 1200,1080 1200,1170 0,1450" fill="var(--accent-green)"/>
    <polygon points="0,2030 1200,1720 1200,1790 0,2100" fill="var(--earth-dark)"/>
    <polygon points="0,2100 1200,1790 1200,2536 0,2536" fill="var(--paper)"/>
    <g transform="rotate(-20 800 1720)">
      <rect x="380" y="1660" width="900" height="150" rx="75" fill="var(--paper)"/>
      <text x="440" y="1640" class="contact-label" font-size="78" font-weight="300" fill="var(--paper)" letter-spacing="3">Phone No</text>
      <text x="450" y="1775" class="contact-number" font-size="120" font-weight="700" fill="var(--earth-mid)" letter-spacing="2">0481657240</text>
    </g>
  </svg>

  <section class="services">
    <div class="bold">Lawn</div>
    <div class="light">Mowing</div>
    <div class="rule"></div>
    <div class="bold">Gardening</div>
    <div class="gap"></div>
    <div class="bold">Green</div>
    <div class="light">Waste Removal</div>
    <div class="rule"></div>
    <div class="bold">Pruning</div>
    <div class="gap"></div>
    <div class="bold">Weeding</div>
    <div class="gap"></div>
    <div class="bold">Vegetable</div>
    <div class="light">Garden Creation</div>
  </section>

  <footer class="brand">
    <div class="brand-dot"></div>
    <div class="brand-name">Greenfield Yard Co</div>
  </footer>
</main>
</body>
</html>
```